Data Analytics Irish company needs Stationery Design

We need a stationery design for our data analytics company based in Dublin called 'Numbryx': we develop innovative web-based corporate applications exploiting advanced Machine Learning and Data Mining techniques.
Like the animal that inspired our company name, the final design should communicate intelligence and passion; on the other hand, we want to keep the highest professional appeal.
We love our current logo and we have tried out several color variations: we prefer solutions (see the logo attached) with white design and dark backgrounds, but we will also be glad to see some designs that follow the colors of the palette of the attached web screenshot.

```html
<!DOCTYPE html>
<html lang="en">
<head>
<meta charset="utf-8">
<title>Numbryx – Letterhead</title>
<link rel="stylesheet" href="https://fonts.googleapis.com/css2?family=Open+Sans:wght@400;600;700&family=Tinos&display=swap">
<style>
  :root {
    --ink: #1f1f1f;
    --body: #333333;
    --muted: #444444;
    --watermark: #e6e6e6;
    --rule: #8a8a8a;
    --paper: #ffffff;
  }
  html, body {
    margin: 0;
    padding: 0;
    overflow: hidden;
    background: var(--paper);
  }
  .letterhead {
    position: relative;
    width: 848px;
    height: 1200px;
    overflow: hidden;
    background: var(--paper);
    font-family: "Open Sans", Arial, sans-serif;
    color: var(--body);
  }
  .watermark {
    position: absolute;
    left: -330px;
    top: 360px;
    width: 1000px;
    height: 1000px;
    border-radius: 50%;
    background: var(--watermark);
    opacity: 0.55;
  }
  .brand {
    position: absolute;
    top: 150px;
    left: 0;
    width: 100%;
    display: flex;
    justify-content: center;
    align-items: center;
    gap: 14px;
  }
  .brand-dot {
    width: 30px;
    height: 30px;
    border-radius: 50%;
    background: var(--ink);
  }
  .brand-name {
    font-size: 52px;
    font-weight: 600;
    color: var(--ink);
    letter-spacing: 0.5px;
    line-height: 1;
  }
  .letter {
    position: absolute;
    left: 123px;
    width: 612px;
    top: 286px;
  }
  .salutation {
    margin: 0 0 62px;
    font-size: 20px;
    color: var(--ink);
  }
  .letter-body p {
    margin: 0 0 25px;
    font-size: 15.6px;
    line-height: 25.5px;
    text-align: justify;
    hyphens: auto;
  }
  .signature {
    position: absolute;
    left: 123px;
    top: 956px;
  }
  .signer-name {
    margin: 0;
    font-size: 20px;
    color: var(--ink);
  }
  .signer-title {
    margin: 6px 0 0;
    font-size: 14px;
    color: var(--muted);
  }
  .contact-bar {
    position: absolute;
    top: 1095px;
    left: 0;
    width: 100%;
    height: 58px;
    font-family: "Tinos", "Times New Roman", serif;
    font-size: 14.5px;
    line-height: 21px;
    color: var(--ink);
  }
  .contact-bar .col { position: absolute; top: 12px; }
  .contact-address { left: 130px; width: 180px; text-align: center; }
  .contact-phone { left: 382px; top: 14px !important; }
  .contact-web { left: 578px; top: 4px !important; line-height: 26px; }
  .divider {
    position: absolute;
    top: 0;
    width: 2px;
    height: 58px;
    background: var(--rule);
  }
  .divider.first { left: 330px; }
  .divider.second { left: 528px; }
</style>
</head>
<body>
<main class="letterhead">
  <div class="watermark" aria-hidden="true"></div>

  <header class="brand">
    <span class="brand-dot" aria-hidden="true"></span>
    <span class="brand-name">Numbryx</span>
  </header>

  <section class="letter">
    <p class="salutation">Dear Mr. Smith,</p>
    <div class="letter-body">
      <p>Lorem ipsum dolor sit amet, consectetur adipiscing elit. Donec orci purus, luctus vitae dignissim eu, iaculis sed purus. Vivamus faucibus, ipsum nec aliquet viverra, leo mauris condimentum ligula, sit amet sagittis enim ligula quis arcu. Nam egestas tortor id nisi porttitor mattis. In tortor ante, ultricies in suscipit a, tempus non massa. Vivamus et auctor mi. Fusce vel massa nulla. Phasellus nec eros mauris, et scelerisque orci. Donec malesuada orci vitae nulla accumsan porta a id massa. Quisque accumsan iaculis magna sit amet fringilla. Maecenas consequat, magna eget tincidunt semper, odio nibh rutrum mi, id feugiat ante nisi eu risus. Vestibulum nunc orci, rhoncus a placerat in, ultricies in mi. Cras mattis varius eros, vel fringilla nisi suscipit eget.</p>
      <p>Quisque scelerisque sagittis nulla at porttitor. Mauris a justo et tellus interdum tristique. Sed id augue vitae urna euismod commodo aliquet a quam. Pellentesque arcu velit, cursus et malesuada ut, consequat et diam. Nullam erat sem, rhoncus id ullamcorper vitae, rhoncus et arcu. In ultricies ultricies nulla, ut rutrum nisi iaculis at. Donec eu magna a metus ornare faucibus. Fusce aliquet faucibus ultricies. Morbi semper, est id tincidunt gravida, sem arcu adipiscing lacus, ac bibendum nulla leo eu purus. Quisque nec diam sed risus consectetur a ccumsan quis quis nibh. Vestibulum id purus lorem.</p>
    </div>
  </section>

  <section class="signature">
    <p class="signer-name">John Doe</p>
    <p class="signer-title">Co-Founder &amp; CEO</p>
  </section>

  <footer class="contact-bar">
    <div class="col contact-address">14 Larkfield Row,<br>Dublin 8, D08 K2P7</div>
    <span class="divider first" aria-hidden="true"></span>
    <div class="col contact-phone">t: 01.482.6630<br>f: 01.482.6631</div>
    <span class="divider second" aria-hidden="true"></span>
    <div class="col contact-web">hello@numbryx.ie<br>www.numbryx.ie</div>
  </footer>
</main>
</body>
</html>
```